Gallic Jest

Creation of a cover for a book on French plays on words.
The public is lovers of the French language
TITLE: The gentle phrases of Honoré Vasseline
SUB-TITLE: Sly words, play on words
PUBLISHER (at the bottom of the page): Editions Plumeau
(See joined examples, previous books of the same author)
Size: 14 x 20.5 cm
Please note that the text on the cover is in French, not in English:
Fine phrases from Honoré Vasseline
Witty words, witty words (subtitle, smaller)
Plumeau Editions

```html
<!DOCTYPE html>
<html lang="en">
<head>
<meta charset="utf-8">
<title>Gallic Jest — Book Cover</title>
<link rel="stylesheet" href="https://fonts.googleapis.com/css2?family=Bebas+Neue&family=Anton&family=Montserrat:wght@600&display=swap">
<style>
  :root {
    --backdrop: #939393;
    --paper: #ffffff;
    --ink: #0a0a0a;
    --author-first: #1fae1f;
    --author-last: #12a4dc;
    --flag-blue: #27168a;
    --flag-white: #dcdad7;
    --flag-red: #c2101a;
    --jest-j: #6600bb;
    --jest-e: #ff0000;
    --jest-s: #ff8800;
    --jest-t: #ffcc00;
    --publisher: #555555;
  }
  * { margin: 0; padding: 0; box-sizing: border-box; }
  html, body {
    width: 1200px;
    height: 1200px;
    overflow: hidden;
    background: var(--backdrop);
  }
  .book-cover {
    position: absolute;
    left: 290px;
    top: 107px;
    width: 669px;
    height: 978px;
    background: var(--paper);
  }
  .author-line,
  .subtitle {
    position: absolute;
    left: 0;
    width: 100%;
    text-align: center;
    font-family: "Anton", sans-serif;
    font-weight: 400;
    font-size: 32px;
    line-height: 44px;
    letter-spacing: -0.6px;
    text-transform: uppercase;
    color: var(--ink);
  }
  .author-line { top: 189px; }
  .subtitle { top: 682px; }
  .author-first { color: var(--author-first); }
  .author-last { color: var(--author-last); }
  .title-art {
    position: absolute;
    left: 0;
    top: 0;
    width: 669px;
    height: 978px;
  }
  .title-word {
    font-family: "Bebas Neue", sans-serif;
    stroke-width: 5;
    stroke-linejoin: round;
  }
  .publisher {
    position: absolute;
    top: 925px;
    left: 0;
    width: 100%;
    text-align: center;
    font-family: "Montserrat", sans-serif;
    font-weight: 600;
    font-size: 14px;
    letter-spacing: 5px;
    text-transform: uppercase;
    color: var(--publisher);
  }
</style>
</head>
<body>
  <main class="book-cover">
    <p class="author-line">The gentle phrases of <span class="author-first">Honoré</span> <span class="author-last">Vasseline</span></p>

    <svg class="title-art" viewBox="0 0 669 978" aria-label="Gallic Jest">
      <defs>
        <linearGradient id="tricolour" x1="61" y1="0" x2="612" y2="0" gradientUnits="userSpaceOnUse">
          <stop offset="0" stop-color="var(--flag-blue)"/>
          <stop offset="0.36" stop-color="var(--flag-blue)"/>
          <stop offset="0.45" stop-color="var(--flag-white)"/>
          <stop offset="0.62" stop-color="var(--flag-white)"/>
          <stop offset="0.72" stop-color="var(--flag-red)"/>
          <stop offset="1" stop-color="#a80c14"/>
        </linearGradient>
      </defs>
      <text class="title-word title-gallic" x="63" y="438" font-size="248" textLength="547" lengthAdjust="spacingAndGlyphs" fill="url(#tricolour)" stroke="url(#tricolour)">GALLIC</text>
      <g class="title-word title-jest" font-size="279">
        <text x="70" y="649" textLength="94" lengthAdjust="spacingAndGlyphs" fill="var(--jest-j)" stroke="var(--jest-j)">J</text>
        <text x="217" y="649" textLength="92" lengthAdjust="spacingAndGlyphs" fill="var(--jest-e)" stroke="var(--jest-e)">E</text>
        <text x="370" y="649" textLength="100" lengthAdjust="spacingAndGlyphs" fill="var(--jest-s)" stroke="var(--jest-s)">S</text>
        <text x="525" y="649" textLength="96" lengthAdjust="spacingAndGlyphs" fill="var(--jest-t)" stroke="var(--jest-t)">T</text>
      </g>
    </svg>

    <p class="subtitle">Sly words, play on words</p>
    <p class="publisher">Editions Plumeau</p>
  </main>
</body>
</html>
```